Home Care App Design

We would like a responsive app design (mobile/web) for an app that will be used by our staff. These need to work display nearly the same for iPhone and Android. The app tracks caregiver tasks (check-in time, daily client activities, caregiver notes, and check out time) and provides updates to team and family members
Updates

I have added individual or grouped pages with better resolution. please let me know if you have any questions

we did not get enough entries so we increase the budget and have not received any new designer entries

Target Market(s)

professional caregivers and family members

Industry/Entity Type

Home Health Care

Font styles to use
Serif

Requirements
Must have
• We currently have a logo - please use colors or slight variants
• We also will need pop-up designs for informational messages and call to actions (with 1-3 options)
Nice to have
• I have attached a sketch of the app, please use this as a guideline. We are looking for ease of use.
• Please feel free to add design aspects that will make it easy to navigate, select options, or enter notes/messages

```html
<!DOCTYPE html>
<html lang="en">
<head>
<meta charset="utf-8">
<title>Tendwell – Caregiver App Screens</title>
<link href="https://fonts.googleapis.com/css2?family=Lato:wght@400;700;900&display=swap" rel="stylesheet">
<style>
:root{
  --bg:#eef1f3;
  --teal-dark:#2f5d72;
  --teal:#3f7590;
  --teal-light:#5b97b0;
  --cyan:#3fb8dd;
  --cyan-soft:#8fd6ec;
  --white:#ffffff;
  --ink:#2c3e4a;
  --muted:#8a98a2;
  --line:#e2e7ea;
  --star:#f3b73b;
  --photo-a:#b9c6cd;
  --photo-b:#8fa2ad;
}
*{box-sizing:border-box;margin:0;padding:0}
html,body{width:880px;height:1200px;overflow:hidden}
body{background:var(--bg);font-family:"Lato",sans-serif;color:var(--ink);position:relative}
.screen{position:absolute;width:274px;background:var(--white);overflow:hidden;box-shadow:0 4px 14px rgba(30,60,80,.18)}
.top{top:16px;height:570px}
.bottom{top:618px;height:566px}
.s-login{left:14px;background:linear-gradient(160deg,var(--teal-light),var(--teal-dark))}
.s-home{left:303px}
.s-clients{left:592px}
.s-team{left:152px}
.s-time{left:454px}

/* login */
.brand{font-weight:700;color:var(--white);font-size:19px;letter-spacing:.4px;position:absolute;left:20px;top:30px}
.login-mark{position:absolute;left:87px;top:130px;width:100px;height:100px;border-radius:50%;background:rgba(255,255,255,.12);box-shadow:0 0 0 10px rgba(255,255,255,.06)}
.login-mark::after{content:"";position:absolute;inset:18px;border-radius:50%;background:var(--cyan-soft);opacity:.55}
.field-label{position:absolute;left:24px;font-size:7px;color:rgba(255,255,255,.8);letter-spacing:.6px;text-transform:uppercase}
.field{position:absolute;left:24px;width:226px;height:24px;background:var(--white);border-radius:2px}
.btn{position:absolute;height:24px;border-radius:12px;background:var(--cyan);color:var(--white);font-size:9px;font-weight:700;letter-spacing:1px;display:flex;align-items:center;justify-content:center}
.forgot{position:absolute;width:100%;text-align:center;top:392px;font-size:8px;color:rgba(255,255,255,.8)}

/* shared header */
.header{position:absolute;left:0;top:0;width:100%;background:linear-gradient(170deg,var(--teal-light),var(--teal))}
.header svg.wave{position:absolute;left:0;bottom:-1px;width:100%;height:28px}
.mini-brand{position:absolute;left:12px;top:12px;width:14px;height:14px;border-radius:50%;background:var(--white);opacity:.9}
.menu{position:absolute;right:12px;top:13px;width:12px}
.menu i{display:block;height:1.5px;background:var(--white);margin-bottom:3px}
.title{position:absolute;width:100%;text-align:center;top:13px;color:var(--white);font-size:10px;font-weight:700;letter-spacing:1.5px}

.photo{border-radius:50%;background:linear-gradient(150deg,var(--photo-a),var(--photo-b))}

/* home */
.profile{position:absolute;left:0;top:18px;width:100%;text-align:center;color:var(--white)}
.profile .photo{width:46px;height:46px;margin:0 auto;border:2px solid var(--white)}
.profile h2{font-size:11px;font-weight:700;margin-top:6px}
.stars{color:var(--star);font-size:9px;letter-spacing:1px}
.stats{position:absolute;top:108px;left:14px;right:14px;display:flex}
.stat{flex:1;text-align:center;color:var(--white);border-right:1px solid rgba(255,255,255,.3)}
.stat:last-child{border:none}
.stat b{display:block;font-size:12px;font-weight:900}
.stat span{font-size:6.5px;opacity:.8}
.schedule{position:absolute;top:190px;left:10px;right:10px;background:var(--white);border-radius:3px;box-shadow:0 2px 8px rgba(0,0,0,.1)}
.schedule-head{display:flex;justify-content:space-between;align-items:center;padding:8px 10px;border-bottom:1px solid var(--line)}
.schedule-head h3{font-size:7.5px;color:var(--cyan);letter-spacing:1px}
.select{font-size:7px;border:1px solid var(--line);padding:2px 16px 2px 5px;position:relative}
.select::after{content:"";position:absolute;right:4px;top:5px;border:3px solid transparent;border-top-color:var(--muted)}
.task{display:flex;gap:8px;padding:10px;border-bottom:1px solid var(--line);align-items:flex-start}
.task svg{flex:none;width:14px;height:14px;margin-top:1px}
.task h4{font-size:10px;font-weight:700}
.task p{font-size:7px;color:var(--muted);margin-top:2px}
.task .when{margin-left:auto;font-size:6.5px;color:var(--muted)}
.fab{position:absolute;right:14px;bottom:52px;width:28px;height:28px;border-radius:50%;background:var(--cyan);color:var(--white);font-size:18px;display:flex;align-items:center;justify-content:center;box-shadow:0 2px 6px rgba(0,0,0,.2)}

/* nav */
.nav{position:absolute;left:0;bottom:0;width:100%;height:40px;background:var(--white);border-top:1px solid var(--line);display:flex}
.nav a{flex:1;display:flex;flex-direction:column;align-items:center;justify-content:center;gap:3px;font-size:6px;color:var(--muted);text-decoration:none}
.nav a svg{width:13px;height:13px}
.nav a.active{background:var(--teal);color:var(--white)}

/* clients */
.client-list{position:absolute;top:46px;left:0;right:0}
.client{display:flex;align-items:center;gap:9px;padding:8px 12px;border-bottom:1px solid var(--line);height:52px}
.client .photo{width:32px;height:32px;flex:none}
.client h4{font-size:10px;font-weight:700}
.client p{font-size:6.5px;color:var(--muted);margin-top:2px;display:flex;align-items:center;gap:3px}
.client p svg{width:6px;height:6px}
.chev{margin-left:auto;width:6px;height:10px}

/* team */
.team-grid{position:absolute;top:150px;left:16px;right:16px;display:grid;grid-template-columns:1fr 1fr;row-gap:44px}
.member{text-align:center}
.member .photo{width:58px;height:58px;margin:0 auto 6px}
.member h4{font-size:9px;font-weight:700}
.member p{font-size:6.5px;color:var(--muted);margin-top:2px}

/* time card */
.tabs{position:absolute;top:48px;left:14px;right:14px;display:flex;border-bottom:1px solid var(--line)}
.tab{flex:1;display:flex;align-items:center;justify-content:center;gap:5px;font-size:7.5px;letter-spacing:1px;color:var(--muted);padding:8px 0}
.tab.active{color:var(--teal);border-bottom:2px solid var(--cyan)}
.tab svg{width:9px;height:9px}
.form{position:absolute;top:196px;left:18px;right:18px}
.form label{display:block;font-size:7px;color:var(--muted);margin:12px 0 4px}
.input{height:24px;border:1px solid var(--line);border-radius:2px;font-size:8px;color:var(--ink);display:flex;align-items:center;justify-content:space-between;padding:0 8px}
.input svg{width:9px;height:9px}
.divider{height:1px;background:var(--line);margin:22px 0 10px}
</style>
</head>
<body>

<!-- Login -->
<section class="screen top s-login">
  <div class="brand">Tendwell</div>
  <div class="login-mark"></div>
  <span class="field-label" style="top:270px">Email</span>
  <div class="field" style="top:280px"></div>
  <span class="field-label" style="top:314px">Password</span>
  <div class="field" style="top:324px"></div>
  <div class="btn" style="left:87px;top:360px;width:100px">LOG IN</div>
  <div class="forgot">Forgot password?</div>
</section>

<!-- Home -->
<section class="screen top s-home">
  <div class="header" style="height:170px">
    <div class="mini-brand"></div>
    <div class="menu"><i></i><i></i><i></i></div>
    <div class="profile">
      <div class="photo" role="img" aria-label="Caregiver profile photo"></div>
      <h2>Nora Whitfield</h2>
      <div class="stars">★★★★★</div>
    </div>
    <div class="stats">
      <div class="stat"><b>6.5</b><span>Hours today</span></div>
      <div class="stat"><b>$95</b><span>Earned week</span></div>
      <div class="stat"><b>4</b><span>Visits left</span></div>
    </div>
    <svg class="wave" viewBox="0 0 274 28" preserveAspectRatio="none"><path d="M0 14 C70 30 150 0 274 12 L274 28 L0 28Z" fill="#fff"/></svg>
  </div>
  <div class="schedule">
    <div class="schedule-head"><h3>SCHEDULE</h3><span class="select">Today</span></div>
    <div class="task">
      <svg viewBox="0 0 14 14"><circle cx="7" cy="7" r="6" fill="none" stroke="#3fb8dd" stroke-width="1.4"/><path d="M4 7l2 2 4-4" fill="none" stroke="#3fb8dd" stroke-width="1.4"/></svg>
      <div><h4>Check in @ Ruth Pemberton</h4><p>9:00 AM · 14 Elm Rd, Placeville</p></div>
      <span class="when">Now</span>
    </div>
    <div class="task">
      <svg viewBox="0 0 14 14"><rect x="2" y="1.5" width="10" height="11" rx="1" fill="none" stroke="#3fb8dd" stroke-width="1.4"/><path d="M4.5 5h5M4.5 8h5" stroke="#3fb8dd" stroke-width="1.2"/></svg>
      <div><h4>Review shift notes</h4><p>Left by Leah Donovan</p></div>
      <span class="when">10:30</span>
    </div>
    <div class="task">
      <svg viewBox="0 0 14 14"><path d="M3 2h3l1 3-2 1a7 7 0 003 3l1-2 3 1v3c-6 1-10-3-9-9z" fill="none" stroke="#3fb8dd" stroke-width="1.3"/></svg>
      <div><h4>Call Owen Prescott</h4><p>(555) 010-2244</p></div>
      <span class="when">1:00</span>
    </div>
  </div>
  <div class="fab">+</div>
  <nav class="nav">
    <a class="active"><svg viewBox="0 0 13 13"><path d="M1 2h11v7H5l-3 3V9H1z" fill="none" stroke="currentColor" stroke-width="1.2"/></svg>Messages</a>
    <a><svg viewBox="0 0 13 13"><path d="M6.5 11.5S1 8 1 4.5A2.7 2.7 0 016.5 3 2.7 2.7 0 0112 4.5c0 3.5-5.5 7-5.5 7z" fill="none" stroke="currentColor" stroke-width="1.2"/></svg>Clients</a>
    <a><svg viewBox="0 0 13 13"><circle cx="4.5" cy="4" r="2" fill="none" stroke="currentColor" stroke-width="1.2"/><circle cx="9" cy="4.5" r="1.7" fill="none" stroke="currentColor" stroke-width="1.2"/><path d="M1 11c0-2.5 1.5-4 3.5-4S8 8.5 8 11M8.5 7.5c2 0 3.5 1 3.5 3.5" fill="none" stroke="currentColor" stroke-width="1.2"/></svg>Team</a>
    <a><svg viewBox="0 0 13 13"><circle cx="6.5" cy="6.5" r="5.5" fill="none" stroke="currentColor" stroke-width="1.2"/><path d="M6.5 3.5v3l2 1.5" fill="none" stroke="currentColor" stroke-width="1.2"/></svg>Time Card</a>
  </nav>
</section>

<!-- Clients -->
<section class="screen top s-clients">
  <div class="header" style="height:52px">
    <div class="mini-brand"></div>
    <div class="title">CLIENTS</div>
    <div class="menu"><i></i><i></i><i></i></div>
    <svg class="wave" viewBox="0 0 274 28" preserveAspectRatio="none"><path d="M0 16 C80 30 160 4 274 16 L274 28 L0 28Z" fill="#fff"/></svg>
  </div>
  <div class="client-list">
    <div class="client"><div class="photo" role="img" aria-label="Client photo"></div><div><h4>Mara Ellison</h4><p><svg viewBox="0 0 6 6"><circle cx="3" cy="2.5" r="2" fill="#3fb8dd"/></svg>22 Oak Ln, Placeville, MA 04409</p><p><svg viewBox="0 0 6 6"><circle cx="3" cy="3" r="2" fill="#3fb8dd"/></svg>Home Care</p></div><svg class="chev" viewBox="0 0 6 10"><path d="M1 1l4 4-4 4" fill="none" stroke="#8a98a2"/></svg></div>
    <div class="client"><div class="photo" role="img" aria-label="Client photo"></div><div><h4>Owen Prescott</h4><p><svg viewBox="0 0 6 6"><circle cx="3" cy="2.5" r="2" fill="#3fb8dd"/></svg>8 Birch Ave, Placeville, MA 04409</p><p><svg viewBox="0 0 6 6"><circle cx="3" cy="3" r="2" fill="#3fb8dd"/></svg>Home Care</p></div><svg class="chev" viewBox="0 0 6 10"><path d="M1 1l4 4-4 4" fill="none" stroke="#8a98a2"/></svg></div>
    <div class="client"><div class="photo" role="img" aria-label="Client photo"></div><div><h4>Tessa Barlow</h4><p><svg viewBox="0 0 6 6"><circle cx="3" cy="2.5" r="2" fill="#3fb8dd"/></svg>41 Pine St, Placeville, MA 04409</p><p><svg viewBox="0 0 6 6"><circle cx="3" cy="3" r="2" fill="#3fb8dd"/></svg>Home Care</p></div><svg class="chev" viewBox="0 0 6 10"><path d="M1 1l4 4-4 4" fill="none" stroke="#8a98a2"/></svg></div>
    <div class="client"><div class="photo" role="img" aria-label="Client photo"></div><div><h4>Calvin Reyes</h4><p><svg viewBox="0 0 6 6"><circle cx="3" cy="2.5" r="2" fill="#3fb8dd"/></svg>17 Cedar Ct, Placeville, MA 04409</p><p><svg viewBox="0 0 6 6"><circle cx="3" cy="3" r="2" fill="#3fb8dd"/></svg>Home Care</p></div><svg class="chev" viewBox="0 0 6 10"><path d="M1 1l4 4-4 4" fill="none" stroke="#8a98a2"/></svg></div>
    <div class="client"><div class="photo" role="img" aria-label="Client photo"></div><div><h4>Hazel Morton</h4><p><svg viewBox="0 0 6 6"><circle cx="3" cy="2.5" r="2" fill="#3fb8dd"/></svg>5 Maple Dr, Placeville, MA 04409</p><p><svg viewBox="0 0 6 6"><circle cx="3" cy="3" r="2" fill="#3fb8dd"/></svg>Home Care</p></div><svg class="chev" viewBox="0 0 6 10"><path d="M1 1l4 4-4 4" fill="none" stroke="#8a98a2"/></svg></div>
    <div class="client"><div class="photo" role="img" aria-label="Client photo"></div><div><h4>Ivy Langford</h4><p><svg viewBox="0 0 6 6"><circle cx="3" cy="2.5" r="2" fill="#3fb8dd"/></svg>63 Ash Way, Placeville, MA 04409</p><p><svg viewBox="0 0 6 6"><circle cx="3" cy="3" r="2" fill="#3fb8dd"/></svg>Home Care</p></div><svg class="chev" viewBox="0 0 6 10"><path d="M1 1l4 4-4 4" fill="none" stroke="#8a98a2"/></svg></div>
    <div class="client"><div class="photo" role="img" aria-label="Client photo"></div><div><h4>Ruth Pemberton</h4><p><svg viewBox="0 0 6 6"><circle cx="3" cy="2.5" r="2" fill="#3fb8dd"/></svg>14 Elm Rd, Placeville, MA 04409</p><p><svg viewBox="0 0 6 6"><circle cx="3" cy="3" r="2" fill="#3fb8dd"/></svg>Home Care</p></div><svg class="chev" viewBox="0 0 6 10"><path d="M1 1l4 4-4 4" fill="none" stroke="#8a98a2"/></svg></div>
  </div>
  <nav class="nav">
    <a><svg viewBox="0 0 13 13"><path d="M1 2h11v7H5l-3 3V9H1z" fill="none" stroke="currentColor" stroke-width="1.2"/></svg>Messages</a>
    <a class="active"><svg viewBox="0 0 13 13"><path d="M6.5 11.5S1 8 1 4.5A2.7 2.7 0 016.5 3 2.7 2.7 0 0112 4.5c0 3.5-5.5 7-5.5 7z" fill="none" stroke="currentColor" stroke-width="1.2"/></svg>Clients</a>
    <a><svg viewBox="0 0 13 13"><circle cx="4.5" cy="4" r="2" fill="none" stroke="currentColor" stroke-width="1.2"/><circle cx="9" cy="4.5" r="1.7" fill="none" stroke="currentColor" stroke-width="1.2"/><path d="M1 11c0-2.5 1.5-4 3.5-4S8 8.5 8 11M8.5 7.5c2 0 3.5 1 3.5 3.5" fill="none" stroke="currentColor" stroke-width="1.2"/></svg>Team</a>
    <a><svg viewBox="0 0 13 13"><circle cx="6.5" cy="6.5" r="5.5" fill="none" stroke="currentColor" stroke-width="1.2"/><path d="M6.5 3.5v3l2 1.5" fill="none" stroke="currentColor" stroke-width="1.2"/></svg>Time Card</a>
  </nav>
</section>

<!-- Team -->
<section class="screen bottom s-team">
  <div class="header" style="height:52px">
    <div class="mini-brand"></div>
    <div class="title">TEAM</div>
    <div class="menu"><i></i><i></i><i></i></div>
    <svg class="wave" viewBox="0 0 274 28" preserveAspectRatio="none"><path d="M0 16 C80 30 160 4 274 16 L274 28 L0 28Z" fill="#fff"/></svg>
  </div>
  <div class="team-grid">
    <div class="member"><div class="photo" role="img" aria-label="Team member photo"></div><h4>Leah Donovan</h4><p>Home Caregiver</p></div>
    <div class="member"><div class="photo" role="img" aria-label="Team member photo"></div><h4>Grace Whitaker</h4><p>Home Caregiver</p></div>
    <div class="member"><div class="photo" role="img" aria-label="Team member photo"></div><h4>Miles Carver</h4><p>Home Caregiver</p></div>
    <div class="member"><div class="photo" role="img" aria-label="Team member photo"></div><h4>Priya Sandell</h4><p>Home Caregiver</p></div>
    <div class="member"><div class="photo" role="img" aria-label="Team member photo"></div><h4>Ethan Brooks</h4><p>Home Caregiver</p></div>
    <div class="member"><div class="photo" role="img" aria-label="Team member photo"></div><h4>Simon Reed</h4><p>Home Caregiver</p></div>
  </div>
  <nav class="nav">
    <a><svg viewBox="0 0 13 13"><path d="M1 2h11v7H5l-3 3V9H1z" fill="none" stroke="currentColor" stroke-width="1.2"/></svg>Messages</a>
    <a><svg viewBox="0 0 13 13"><path d="M6.5 11.5S1 8 1 4.5A2.7 2.7 0 016.5 3 2.7 2.7 0 0112 4.5c0 3.5-5.5 7-5.5 7z" fill="none" stroke="currentColor" stroke-width="1.2"/></svg>Clients</a>
    <a class="active"><svg viewBox="0 0 13 13"><circle cx="4.5" cy="4" r="2" fill="none" stroke="currentColor" stroke-width="1.2"/><circle cx="9" cy="4.5" r="1.7" fill="none" stroke="currentColor" stroke-width="1.2"/><path d="M1 11c0-2.5 1.5-4 3.5-4S8 8.5 8 11M8.5 7.5c2 0 3.5 1 3.5 3.5" fill="none" stroke="currentColor" stroke-width="1.2"/></svg>Team</a>
    <a><svg viewBox="0 0 13 13"><circle cx="6.5" cy="6.5" r="5.5" fill="none" stroke="currentColor" stroke-width="1.2"/><path d="M6.5 3.5v3l2 1.5" fill="none" stroke="currentColor" stroke-width="1.2"/></svg>Time Card</a>
  </nav>
</section>

<!-- Time card -->
<section class="screen bottom s-time">
  <div class="header" style="height:52px">
    <div class="mini-brand"></div>
    <div class="title">TIME CARD</div>
    <div class="menu"><i></i><i></i><i></i></div>
    <svg class="wave" viewBox="0 0 274 28" preserveAspectRatio="none"><path d="M0 16 C80 30 160 4 274 16 L274 28 L0 28Z" fill="#fff"/></svg>
  </div>
  <div class="tabs">
    <div class="tab active"><svg viewBox="0 0 9 9"><path d="M1 8l1-3 5-5 2 2-5 5z" fill="none" stroke="currentColor"/></svg>ENTRY</div>
    <div class="tab"><svg viewBox="0 0 9 9"><circle cx="4.5" cy="4.5" r="3.8" fill="none" stroke="currentColor"/><path d="M4.5 2.5v2l1.5 1" fill="none" stroke="currentColor"/></svg>HISTORY</div>
  </div>
  <div class="form">
    <label>Client</label>
    <div class="input">Ruth Pemberton<svg viewBox="0 0 9 9"><path d="M1 3l3.5 3.5L8 3" fill="none" stroke="#8a98a2"/></svg></div>
    <label>Time</label>
    <div class="input">9:00 AM<svg viewBox="0 0 9 9"><circle cx="4.5" cy="4.5" r="3.8" fill="none" stroke="#8a98a2"/><path d="M4.5 2.5v2l1.5 1" fill="none" stroke="#8a98a2"/></svg></div>
    <div class="divider"></div>
    <label>Start</label>
    <div class="input">May 12, 2024<svg viewBox="0 0 9 9"><rect x=".8" y="1.5" width="7.4" height="6.7" fill="none" stroke="#8a98a2"/><path d="M.8 3.5h7.4" stroke="#8a98a2"/></svg></div>
    <label>End</label>
    <div class="input">May 12, 2024<svg viewBox="0 0 9 9"><rect x=".8" y="1.5" width="7.4" height="6.7" fill="none" stroke="#8a98a2"/><path d="M.8 3.5h7.4" stroke="#8a98a2"/></svg></div>
  </div>
  <div class="btn" style="left:87px;top:470px;width:100px">SAVE</div>
  <nav class="nav">
    <a><svg viewBox="0 0 13 13"><path d="M1 2h11v7H5l-3 3V9H1z" fill="none" stroke="currentColor" stroke-width="1.2"/></svg>Messages</a>
    <a><svg viewBox="0 0 13 13"><path d="M6.5 11.5S1 8 1 4.5A2.7 2.7 0 016.5 3 2.7 2.7 0 0112 4.5c0 3.5-5.5 7-5.5 7z" fill="none" stroke="currentColor" stroke-width="1.2"/></svg>Clients</a>
    <a><svg viewBox="0 0 13 13"><circle cx="4.5" cy="4" r="2" fill="none" stroke="currentColor" stroke-width="1.2"/><circle cx="9" cy="4.5" r="1.7" fill="none" stroke="currentColor" stroke-width="1.2"/><path d="M1 11c0-2.5 1.5-4 3.5-4S8 8.5 8 11M8.5 7.5c2 0 3.5 1 3.5 3.5" fill="none" stroke="currentColor" stroke-width="1.2"/></svg>Team</a>
    <a class="active"><svg viewBox="0 0 13 13"><circle cx="6.5" cy="6.5" r="5.5" fill="none" stroke="currentColor" stroke-width="1.2"/><path d="M6.5 3.5v3l2 1.5" fill="none" stroke="currentColor" stroke-width="1.2"/></svg>Time Card</a>
  </nav>
</section>

</body>
</html>
```